Bref créative
Businesscard + stationary
outstand and cretive master piece!
Bright & Fun-filled
Mariana Tolvaldi
www.pixelharbor-exemplo.com.br
contato@pixelharbor-exemplo.com.br
You need to add to business card:
Skype: pixelharbor.online
Twitter: @PixelHarboron
Secondary text to go below logo: Desenvolvimento Web
On the back of business card goes only the logo and some nice art if applyable
This is the new website layout, so please follow this style to create the businesscard and stationary.
This is teh original logo file in EPS
this is another version of teh logo

```html
<!DOCTYPE html>
<html lang="pt-BR">
<head>
<meta charset="utf-8">
<title>Pixelharbor – cartão de visita</title>
<link rel="stylesheet" href="https://fonts.googleapis.com/css2?family=Open+Sans:wght@400;600&display=swap">
<style>
  :root {
    --page: #ffffff;
    --card-light: #ffffff;
    --card-dark: #000000;
    --edge: #b9b9b9;
    --accent: #3fa9f5;
    --ink: #4a4a4a;
    --ink-soft: #333333;
    --ghost: #eeeeee;
    --on-dark: #ffffff;
  }
  * { box-sizing: border-box; margin: 0; padding: 0; }
  html, body { width: 1200px; height: 368px; overflow: hidden; background: var(--page); }
  body { position: relative; font-family: "Open Sans", Arial, sans-serif; }

  .card {
    position: absolute;
    top: 17px;
    width: 583px;
    height: 331px;
    border-radius: 26px;
    overflow: hidden;
  }
  .card--front { left: 7px; background: var(--card-light); border: 2px solid var(--edge); }
  .card--back { left: 614px; background: var(--card-dark); }

  .tab { position: absolute; width: 12px; background: var(--accent); border-radius: 0 4px 4px 0; }
  .tab--left { left: 0; top: 55px; height: 62px; }
  .tab--right { right: 0; top: 193px; height: 90px; border-radius: 4px 0 0 4px; }

  .holder { position: absolute; left: 24px; top: 86px; font-size: 17px; color: var(--ink-soft); }
  .holder .surname { color: var(--accent); }

  .brand { position: absolute; display: flex; align-items: center; gap: 8px; font-weight: 600; letter-spacing: -0.5px; }
  .brand__dot { border-radius: 50%; background: var(--accent); flex: none; }

  .brand--front { right: 18px; top: 62px; font-size: 40px; color: var(--ink); }
  .brand--front .brand__dot { width: 20px; height: 20px; }

  .brand--ghost { right: 14px; top: 242px; font-size: 38px; color: var(--ghost); }
  .brand--ghost .brand__dot { width: 18px; height: 18px; background: var(--ghost); }

  .contact { position: absolute; left: 24px; top: 236px; font-size: 13.5px; line-height: 19px; color: var(--ink-soft); white-space: nowrap; }
  .contact .web { color: var(--accent); }

  .brand--back { left: 0; right: 0; top: 138px; justify-content: center; font-size: 46px; color: var(--on-dark); }
  .brand--back .brand__dot { width: 22px; height: 22px; }

  .social { position: absolute; left: 0; right: 0; top: 257px; text-align: center; font-size: 15px; line-height: 21px; color: var(--on-dark); }
</style>
</head>
<body>
  <section class="card card--front">
    <span class="tab tab--left"></span>
    <span class="tab tab--right"></span>

    <p class="holder">Mariana <span class="surname">Tolvaldi</span></p>

    <div class="brand brand--front"><span>pixelharbor</span><span class="brand__dot"></span></div>
    <div class="brand brand--ghost" aria-hidden="true"><span>pixelharbor</span><span class="brand__dot"></span></div>

    <div class="contact">
      <p>Phone: 11 3000 1234</p>
      <p>Cell: 11 9000 5678</p>
      <p>Email: contato@pixelharbor-exemplo.com.br</p>
      <p class="web">www.pixelharbor-exemplo.com.br</p>
    </div>
  </section>

  <section class="card card--back">
    <div class="brand brand--back"><span>pixelharbor</span><span class="brand__dot"></span></div>
    <div class="social">
      <p>Skype: pixelharbor.online</p>
      <p>Twitter: @PixelHarboron</p>
    </div>
  </section>
</body>
</html>
```